'Quarrystone Co' Business Cards

Quarrystone Co is a clothing company geared toward people in the mining industry who are crushing it (literally) We need a design for a business card that has 'QS' similar to the layout of the inspo photo below. Rock textures and maybe some rock dust (see GIF). I Included SVG of our circle logo but not sure how to include without it being boring, would like some ideas. Front should say 'Quarrystone Co.' (and 'clothing' in smaller letters below) Back should have our webpage 'quarrystoneco.ca' our email 'info@quarrystoneco.ca' plus a FB and IG icon

```html
<!DOCTYPE html>
<html lang="en">
<head>
<meta charset="utf-8">
<title>Quarrystone Co – Business Cards</title>
<link rel="stylesheet" href="https://fonts.googleapis.com/css2?family=Archivo+Black&family=Roboto+Condensed:wght@400;700&display=swap">
<style>
  :root {
    --page-bg: #cfcdcb;
    --card-dark: #2c2c2d;
    --card-darker: #1a1a1b;
    --strip-black: #0b0b0b;
    --brand-green: #5fae3f;
    --brand-green-deep: #3d7f2c;
    --logo-green: #86bb2c;
    --text-light: #f2f2f2;
    --text-muted: #b8b8b8;
  }
  * { box-sizing: border-box; margin: 0; padding: 0; }
  html, body { width: 1200px; height: 1200px; overflow: hidden; }
  body {
    background: var(--page-bg);
    font-family: "Roboto Condensed", sans-serif;
    position: relative;
  }
  .card {
    position: absolute;
    left: 242px;
    width: 703px;
    height: 400px;
    background: radial-gradient(circle at 40% 40%, #363637, var(--card-dark) 60%, #262627);
    overflow: hidden;
  }
  .card--front { top: 170px; }
  .card--back { top: 629px; }

  .rock-texture {
    position: absolute;
    inset: 0 120px 0 0;
    background:
      radial-gradient(circle at 20% 50%, #3a3a3b 0 30%, transparent 45%),
      radial-gradient(ellipse at 60% 55%, #1d1d1e 0 20%, transparent 50%),
      linear-gradient(135deg, #333334, #262627 60%, #2e2e2f);
  }
  .logo-seat {
    position: absolute;
    left: 45px;
    top: 55px;
    width: 290px;
    height: 290px;
    border-radius: 50%;
    background: #2a2a2b;
    border: 14px solid #3b3b3c;
    display: flex;
    align-items: center;
    justify-content: center;
  }
  .logo-seat__circle {
    width: 250px;
    height: 250px;
    border-radius: 50%;
    background: var(--logo-green);
    display: flex;
    align-items: center;
    justify-content: center;
    font-family: "Archivo Black", sans-serif;
    font-size: 96px;
    color: var(--card-dark);
  }

  .brand-strip {
    position: absolute;
    top: 0;
    right: 0;
    width: 120px;
    height: 100%;
  }
  .brand-strip--black { background: linear-gradient(160deg, #1e1e1e, var(--strip-black) 40%); }
  .brand-strip--green { background: linear-gradient(160deg, var(--brand-green), var(--brand-green-deep)); }
  .wordmark {
    position: absolute;
    left: 50%;
    top: 50%;
    transform: translate(-50%, -50%) rotate(-90deg);
    white-space: nowrap;
    text-align: left;
  }
  .wordmark__name {
    display: block;
    font-family: "Archivo Black", sans-serif;
    font-size: 30px;
    letter-spacing: 0.5px;
    line-height: 1;
  }
  .wordmark__tag {
    display: block;
    font-size: 11px;
    letter-spacing: 3px;
    margin-top: 6px;
    text-align: center;
  }
  .brand-strip--black .wordmark__name { color: var(--text-light); }
  .brand-strip--black .wordmark__tag { color: var(--text-muted); }
  .brand-strip--green .wordmark__name { color: var(--strip-black); }
  .brand-strip--green .wordmark__tag { color: var(--strip-black); }

  .contact {
    position: absolute;
    left: 0;
    width: 583px;
    top: 80px;
    text-align: center;
  }
  .contact__icons {
    display: flex;
    justify-content: center;
    gap: 14px;
    margin-bottom: 18px;
  }
  .contact__icons svg { width: 34px; height: 34px; display: block; }
  .contact__line {
    color: var(--text-light);
    font-weight: 700;
    font-size: 21px;
    letter-spacing: 2.5px;
    line-height: 34px;
  }
  .social__label {
    margin-top: 58px;
    color: var(--brand-green);
    font-weight: 700;
    font-size: 15px;
    letter-spacing: 1px;
  }
  .social__pill {
    display: inline-block;
    margin-top: 14px;
    padding: 0 16px;
    height: 40px;
    line-height: 40px;
    border-radius: 20px;
    background: var(--text-light);
    color: var(--strip-black);
    font-weight: 700;
    font-size: 15px;
    letter-spacing: 0.5px;
  }
</style>
</head>
<body>
  <section class="card card--front">
    <div class="rock-texture" role="img" aria-label="Shattered dark rock texture with flying rock fragments and dust"></div>
    <div class="logo-seat">
      <div class="logo-seat__circle">QS</div>
    </div>
    <div class="brand-strip brand-strip--black">
      <div class="wordmark">
        <span class="wordmark__name">QUARRYSTONE CO</span>
        <span class="wordmark__tag">CLOTHING</span>
      </div>
    </div>
  </section>

  <section class="card card--back">
    <div class="contact">
      <div class="contact__icons">
        <svg viewBox="0 0 34 34" aria-label="Website">
          <circle cx="17" cy="17" r="17" fill="var(--brand-green)"/>
          <g fill="none" stroke="#2c2c2d" stroke-width="2">
            <circle cx="17" cy="17" r="10"/>
            <ellipse cx="17" cy="17" rx="4.5" ry="10"/>
            <line x1="7" y1="17" x2="27" y2="17"/>
          </g>
        </svg>
        <svg viewBox="0 0 34 34" aria-label="Email">
          <circle cx="17" cy="17" r="17" fill="var(--brand-green)"/>
          <g fill="none" stroke="#2c2c2d" stroke-width="2" stroke-linejoin="round">
            <rect x="8" y="11" width="18" height="13" rx="1.5"/>
            <polyline points="8,12 17,19 26,12"/>
          </g>
        </svg>
      </div>
      <p class="contact__line">QUARRYSTONECO.CA</p>
      <p class="contact__line">INFO@QUARRYSTONECO.CA</p>
      <p class="social__label">FIND US ON</p>
      <span class="social__pill">Linkwall · Photoloop</span>
    </div>
    <div class="brand-strip brand-strip--green">
      <div class="wordmark">
        <span class="wordmark__name">QUARRYSTONE CO</span>
        <span class="wordmark__tag">CLOTHING</span>
      </div>
    </div>
  </section>
</body>
</html>
```